" Apoio para empresas que desejam vender produtos e/ou serviços para órgãos públicos ou empresas que utilizam processos licitatórios em suas compras "

```html
<!DOCTYPE html>
<html lang="pt-BR">
<head>
<meta charset="UTF-8">
<title>Certamia — Cartão de Visita</title>
<link href="https://fonts.googleapis.com/css2?family=Poppins:wght@400;500;600&display=swap" rel="stylesheet">
<style>
  :root {
    --navy: #0f1240;
    --teal: #2bb3a0;
    --teal-dark: #1f8f80;
    --ink: #1d1f3a;
    --paper: #ffffff;
    --backdrop: #eeeeee;
  }
  * { box-sizing: border-box; margin: 0; padding: 0; }
  html, body { width: 1200px; height: 1200px; overflow: hidden; }
  body {
    background: var(--backdrop);
    font-family: "Poppins", Arial, sans-serif;
    position: relative;
  }
  .card {
    position: absolute;
    left: 170px;
    width: 860px;
    height: 472px;
    overflow: hidden;
  }
  .card--front { top: 110px; background: var(--navy); }
  .card--back { top: 616px; background: var(--paper); }

  /* Front */
  .brand {
    position: absolute;
    left: 0; right: 0; top: 170px;
    display: flex; flex-direction: column; align-items: center;
  }
  .brand__row { display: flex; align-items: center; gap: 22px; }
  .brand__mark {
    width: 70px; height: 70px; border-radius: 50%;
    background: var(--paper);
  }
  .brand__name {
    color: var(--paper);
    font-weight: 600;
    font-size: 66px;
    letter-spacing: 2px;
    line-height: 1;
  }
  .brand__tagline {
    margin-top: 8px;
    margin-left: 92px;
    color: var(--teal);
    font-size: 19px;
    letter-spacing: 3.5px;
    text-transform: uppercase;
  }
  .front-tab { position: absolute; left: 0; bottom: 0; }

  /* Back */
  .accent-bar {
    position: absolute; left: 0; top: 182px;
    width: 12px; height: 190px; background: var(--teal);
  }
  .holder { position: absolute; left: 72px; top: 88px; }
  .holder__name {
    color: var(--navy); font-weight: 600; font-size: 29px; line-height: 1.2;
  }
  .holder__role {
    margin-top: 4px;
    color: var(--teal); font-size: 14px; letter-spacing: 3.4px;
    text-transform: uppercase; text-align: center; font-weight: 500;
  }
  .contacts {
    position: absolute; left: 92px; top: 188px;
    list-style: none; color: var(--ink); font-size: 17px; line-height: 31px;
  }
  .contacts li { display: flex; align-items: flex-start; gap: 12px; }
  .contacts li + li { margin-top: 6px; }
  .contacts svg { flex: none; margin-top: 7px; }
  .decor-mark {
    position: absolute; left: 560px; top: 80px;
    width: 300px; height: 300px; border-radius: 50%;
    background: var(--navy);
  }
</style>
</head>
<body>
  <section class="card card--front">
    <div class="brand">
      <div class="brand__row">
        <span class="brand__mark"></span>
        <span class="brand__name">CERTAMIA</span>
      </div>
      <span class="brand__tagline">Soluções em Licitações</span>
    </div>
    <svg class="front-tab" width="860" height="472" viewBox="0 0 860 472" aria-hidden="true">
      <polygon points="126,472 140,452 710,452 724,472" fill="var(--teal)"/>
    </svg>
  </section>

  <section class="card card--back">
    <div class="accent-bar"></div>
    <div class="holder">
      <h1 class="holder__name">Marina Costa Vieira</h1>
      <p class="holder__role">Diretora de Operações</p>
    </div>
    <ul class="contacts">
      <li>
        <svg width="18" height="18" viewBox="0 0 24 24" aria-hidden="true"><path d="M6.6 10.8a15.1 15.1 0 0 0 6.6 6.6l2.2-2.2a1 1 0 0 1 1-.25 11.4 11.4 0 0 0 3.6.57 1 1 0 0 1 1 1V20a1 1 0 0 1-1 1A17 17 0 0 1 3 4a1 1 0 0 1 1-1h3.5a1 1 0 0 1 1 1c0 1.25.2 2.45.57 3.57a1 1 0 0 1-.25 1z" fill="none" stroke="var(--teal-dark)" stroke-width="2"/></svg>
        <span>(11) 90000-1234</span>
      </li>
      <li>
        <svg width="18" height="18" viewBox="0 0 24 24" aria-hidden="true"><path d="M12 2a7 7 0 0 0-7 7c0 5 7 13 7 13s7-8 7-13a7 7 0 0 0-7-7z" fill="none" stroke="var(--teal-dark)" stroke-width="2"/><circle cx="12" cy="9" r="2.5" fill="var(--teal-dark)"/></svg>
        <span>Rua das Acácias, 120 - 3º Andar<br>Edifício Aurora, Centro,<br>Campinas - SP 13010-000</span>
      </li>
      <li>
        <svg width="18" height="18" viewBox="0 0 24 24" aria-hidden="true"><rect x="3" y="5" width="18" height="14" rx="1.5" fill="none" stroke="var(--teal-dark)" stroke-width="2"/><path d="M3 6l9 7 9-7" fill="none" stroke="var(--teal-dark)" stroke-width="2"/></svg>
        <span>marina.vieira@certamia.com</span>
      </li>
    </ul>
    <div class="decor-mark" aria-hidden="true"></div>
  </section>
</body>
</html>
```